Promotional Ad/Flyer - Kavo Leasing

A division of our company, Kavo Leasing (kavo-leasing.example) is celebrating its 1-year anniversary in September and we would like to run a promotion. I am looking to have a promotional ad/flyer made-up for email mailings and LinkedIn posts and possibly have on our site. Have plenty of product photos to share if needed, not a prerequisite to use our product in the ad but open to it. Can also be cool graphics as well. We want to capture the viewers attention with the 30 DAYS FREE! The message is simple:
We are celebrating our 1-Year Anniversary by offering a Special Peak-Season Promotion!

FREE RENTALS for 30 days with a minimum 30-Day rental!

Valid from Sep. 1 - Dec. 31 & while supplies last.

Please contact our sales department for more details.

Email: quotes@kavo-leasing.example
Phone: +1-555-284-9317

```html
<!DOCTYPE html>
<html lang="en">
<head>
<meta charset="utf-8">
<title>Kavo Leasing – 30 Days Free</title>
<link href="https://fonts.googleapis.com/css2?family=Fira+Sans:wght@300;400;600;700&family=Oswald:wght@500;600&display=swap" rel="stylesheet">
<style>
  :root{
    --page:#e9e9ea;
    --white:#ffffff;
    --navy:#2f3d57;
    --brand:#4a6db4;
    --brand-light:#82a9dd;
    --text-blue:#3d5fa8;
    --muted-blue:#6f92cf;
    --sky-top:#2f74c6;
    --sky-low:#9cc3ea;
    --metal:#8f969e;
  }
  *{margin:0;padding:0;box-sizing:border-box}
  html,body{width:1200px;height:780px;overflow:hidden;background:var(--page)}
  .flyer{position:absolute;left:314px;top:20px;width:572px;height:740px;background:var(--white);
    box-shadow:0 6px 18px rgba(0,0,0,.18);overflow:hidden;font-family:"Fira Sans",sans-serif}
  .hero-photo{position:absolute;left:0;top:0;width:572px;height:370px;
    background:linear-gradient(160deg,var(--sky-top) 0%,var(--sky-low) 45%,var(--metal) 70%,#6d747c 100%)}
  .logo-band{position:absolute;left:0;top:0;width:572px;height:100px;background:var(--white);
    clip-path:polygon(0 0,335px 0,262px 93px,0 93px)}
  .brand{position:absolute;left:24px;top:36px;display:flex;align-items:center;gap:10px}
  .brand-square{width:28px;height:28px;background:var(--brand)}
  .brand-name{font-weight:700;font-size:28px;color:var(--navy);letter-spacing:.3px;line-height:1}
  .brand-tag{position:absolute;left:140px;top:72px;font-size:5.5px;color:var(--navy);letter-spacing:.3px;white-space:nowrap}
  .hero-copy{position:absolute;left:25px;top:115px;width:230px;color:var(--white);font-weight:600;font-size:15px;line-height:1.37}

  .icon-panel{position:absolute;left:20px;top:309px;width:151px;height:349px;background:var(--brand);border-radius:6px;
    color:var(--white);text-align:center}
  .icon-item{position:absolute;left:0;width:100%;font-weight:600;font-size:12px;letter-spacing:.4px;line-height:14px}
  .icon-item svg{display:block;margin:0 auto 6px}
  .icon-container{top:18px}
  .icon-pallets{top:142px}
  .icon-accessories{top:242px}

  .promo-banner{position:absolute;left:236px;top:342px;width:322px;height:54px;background:var(--brand-light);
    clip-path:polygon(26px 0,100% 0,calc(100% - 26px) 100%,0 100%);
    color:var(--white);font-family:"Oswald",sans-serif;font-weight:500;font-size:29px;
    display:flex;align-items:center;justify-content:center;letter-spacing:.5px}

  .offer-lead,.offer-headline,.offer-terms,.offer-validity{position:absolute;left:190px;width:380px;text-align:center;white-space:nowrap}
  .offer-lead{top:432px;font-weight:600;font-size:13.2px;color:var(--text-blue);line-height:1.45;letter-spacing:.2px}
  .offer-headline{top:476px;font-family:"Oswald",sans-serif;font-weight:600;font-size:78px;color:var(--navy);line-height:1;
    transform:scaleX(.7);transform-origin:center top}
  .offer-terms{top:572px;font-family:"Oswald",sans-serif;font-weight:500;font-size:16px;color:var(--text-blue);letter-spacing:-.2px;line-height:1.2}
  .offer-validity{top:605px;font-weight:300;font-size:11.5px;color:var(--muted-blue)}

  .sales-note{position:absolute;left:3px;top:673px;width:325px;height:56px;background:var(--brand-light);
    clip-path:polygon(0 0,290px 0,325px 100%,18px 100%);color:var(--white);font-weight:300;font-size:11.8px;line-height:1.4;padding:15px 0 0 38px}
  .sales-note svg{vertical-align:-2px;margin:0 3px 0 4px}
  .contact-bar{position:absolute;left:307px;top:664px;width:265px;height:76px;background:var(--brand);
    clip-path:polygon(22px 0,100% 0,100% 100%,0 100%,36px 50%,16px 8px)}
  .contact-list{position:absolute;right:14px;top:670px;list-style:none;text-align:right;color:var(--white);font-size:13px;letter-spacing:.5px;line-height:20px;white-space:nowrap}
  .contact-list svg{vertical-align:-2px;margin-left:6px}
</style>
</head>
<body>
<main class="flyer">
  <div class="hero-photo" role="img" aria-label="Photo of stacked aircraft cargo containers and blue pallets against a bright blue sky"></div>
  <div class="logo-band"></div>
  <div class="brand"><span class="brand-square"></span><span class="brand-name">Kavo Leasing</span></div>
  <div class="brand-tag">KAVO-LEASING.EXAMPLE | BY NORVANE GROUP</div>
  <p class="hero-copy">Don’t miss out on revenue opportunities. Rent from us to generate more payload!</p>

  <section class="icon-panel">
    <div class="icon-item icon-container">
      <svg width="76" height="74" viewBox="0 0 80 78" fill="none" stroke="#fff" stroke-width="3" stroke-linejoin="round">
        <path d="M6 26 L40 10 L74 22 L74 56 L40 72 L6 60 Z"/><path d="M6 26 L40 38 L74 22"/><path d="M40 38 V72"/>
        <path d="M48 35 V66 M56 32 V62 M64 28 V59"/><path d="M16 35 V60 M28 39 V65"/>
      </svg>CONTAINER</div>
    <div class="icon-item icon-pallets">
      <svg width="74" height="62" viewBox="0 0 80 66" fill="none" stroke="#fff" stroke-width="2.5">
        <rect x="4" y="3" width="72" height="60"/><path d="M4 23 H76 M4 43 H76 M20 3 V63 M40 3 V63 M60 3 V63"/>
      </svg>PALLETS</div>
    <div class="icon-item icon-accessories">
      <svg width="70" height="70" viewBox="0 0 76 76" fill="none" stroke="#fff" stroke-width="2.5">
        <path d="M38 2 L74 38 L38 74 L2 38 Z"/>
        <path d="M20 20 L56 56 M29 11 L65 47 M11 29 L47 65 M56 20 L20 56 M47 11 L11 47 M65 29 L29 65"/>
      </svg>ACCESSORIES</div>
  </section>

  <div class="promo-banner">FREE RENTALS</div>

  <p class="offer-lead">WE ARE CELEBRATING OUR 1-YEAR ANNIVERSARY<br>BY OFFERING A SPECIAL PEAK-SEASON PROMOTION!</p>
  <h1 class="offer-headline">30 DAYS FREE!</h1>
  <p class="offer-terms">FREE RENTALS FOR 30 DAYS WITH A MINIMUM 30-DAY RENTAL!</p>
  <p class="offer-validity">Valid from Sep. 1 - Dec. 31 and while supplies last.</p>

  <div class="sales-note">PLEASE CONTACT OUR SALES DEPARTMENT<br>FOR MORE DETAILS
    <svg width="12" height="12" viewBox="0 0 12 12" fill="none" stroke="#fff" stroke-width="1"><circle cx="6" cy="6" r="5.3"/><path d="M4 3.2 L5 5 L4.5 5.6 Q5.3 7 6.5 7.6 L7 7 L8.8 8 L8.2 9 Q5 9 3 4 Z" fill="#fff"/></svg>+1-555-284-9317</div>

  <div class="contact-bar"></div>
  <ul class="contact-list">
    <li>+1-555-284-9317<svg width="12" height="12" viewBox="0 0 12 12" fill="none" stroke="#fff"><circle cx="6" cy="6" r="5.3"/><path d="M4 3.2 L5 5 L4.5 5.6 Q5.3 7 6.5 7.6 L7 7 L8.8 8 L8.2 9 Q5 9 3 4 Z" fill="#fff"/></svg></li>
    <li>quotes@kavo-leasing.example<svg width="12" height="12" viewBox="0 0 12 12" fill="none" stroke="#fff"><circle cx="6" cy="6" r="5.3"/><rect x="3" y="4" width="6" height="4" fill="#fff"/></svg></li>
    <li>www.kavo-leasing.example<svg width="12" height="12" viewBox="0 0 12 12" fill="none" stroke="#fff"><circle cx="6" cy="6" r="5.3"/><circle cx="6" cy="6" r="2.8"/><path d="M3.2 6 H8.8"/></svg></li>
  </ul>
</main>
</body>
</html>
```